Design professional label for greener chemicals (cleaning and lubrication) brand

Design a b2b professional label that is based on the examples given.
Size: 135 x 200 mm, please use text of the label description doc (only the kaltro stainless steel polish example design document has the right text and size)
It should include:
1. Logo, can be fully changed except the shape of "KALTRO", colors and fonts of the rest can be customized
2. Focus should be on professional market, we would like to express the professionalism and high quality of the product
3. Focus should be on our brand name "KALTRO BRIGHTER COMPOUNDS"
4. Should include product name, product description, danger sentences, danger symbol, user instructions, image
5. Should include numbers that explain what the product does: 1. Prewash 2. Clean 3. Protect 4. Preserve and highlight number 2.

Target Market(s)

Professional cleaning companies, steel industry, food industry, pharmacy industry

Industry/Entity Type

Cleaning industry, steel industry, food industry, boat cleaning, car cleaning, professional lubrication

Font styles to use
Sans Serif

Requirements
Must have
• Professional look, clean look, image, focus on our brand name
Nice to have
• Numbers (see explanation), label divided in three parts (logo and product name and image in the middle as the highlight)

```html
<!DOCTYPE html>
<html lang="en">
<head>
<meta charset="utf-8">
<title>Kaltro Stainless Steel Polish</title>
<link rel="stylesheet" href="https://fonts.googleapis.com/css2?family=Alfa+Slab+One&family=Oswald:wght@500;600&display=swap">
<style>
  :root {
    --ink: #0d111b;
    --navy: #1b365d;
    --teal: #0f8196;
    --white: #ffffff;
    --steel-light: #e9eaec;
    --steel-mid: #9ea3a8;
    --cloth-green: #3dae77;
    --page: #f2f2f2;
  }
  * { margin: 0; padding: 0; box-sizing: border-box; }
  html, body { width: 869px; height: 1200px; overflow: hidden; background: var(--page); }
  .label {
    position: relative;
    width: 869px;
    height: 1200px;
    overflow: hidden;
    background: var(--ink);
  }
  .hero-photo {
    position: absolute;
    inset: 0 0 auto 0;
    height: 720px;
    background:
      radial-gradient(ellipse 220px 180px at 520px 300px, rgba(61,174,119,.55), transparent 70%),
      linear-gradient(135deg, var(--steel-mid) 0%, #c9cccf 35%, var(--steel-light) 60%, #ffffff 100%);
  }
  .shapes { position: absolute; inset: 0; }
  .brand {
    position: absolute;
    right: 43px;
    top: 60px;
    text-align: right;
    font-family: "Oswald", sans-serif;
    font-weight: 600;
    color: var(--navy);
    line-height: 1;
  }
  .brand-name { font-size: 78px; letter-spacing: 1px; }
  .brand-tagline { font-size: 19px; margin-top: 4px; letter-spacing: .3px; }
  .uses {
    position: absolute;
    left: 73px;
    top: 240px;
    width: 137px;
    list-style: none;
    font-family: "Oswald", sans-serif;
    font-weight: 500;
    color: var(--white);
    text-align: center;
    font-size: 13px;
    line-height: 1.05;
  }
  .uses li { padding: 10px 0 10px; }
  .uses li + li { border-top: 2px solid var(--white); margin: 0 14px; }
  .uses li:first-child { margin: 0 14px; }
  .uses svg { display: block; margin: 0 auto 6px; }
  .copy { position: absolute; inset: 0; }
  .copy text { font-family: "Alfa Slab One", serif; }
</style>
</head>
<body>
<main class="label">
  <div class="hero-photo" role="img" aria-label="Gloved hand wiping a stainless steel surface with a green microfibre cloth"></div>

  <svg class="shapes" width="869" height="1200" viewBox="0 0 869 1200" aria-hidden="true">
    <polygon points="0,52 562,716 869,488 869,1200 0,1200" fill="var(--ink)"/>
    <polyline points="0,40 562,703 869,476" fill="none" stroke="var(--teal)" stroke-width="8"/>
    <polygon points="362,498 394,666 869,386 869,200" fill="var(--navy)"/>
    <polygon points="73,140 210,300 210,624 141,574 73,624" fill="var(--teal)"/>
    <rect x="0" y="1101" width="869" height="52" fill="var(--teal)"/>
    <circle class="eco-badge" cx="190" cy="1125" r="45" fill="var(--ink)"/>
  </svg>

  <div class="brand">
    <div class="brand-name">KALTRO</div>
    <div class="brand-tagline">BRIGHTER COMPOUNDS</div>
  </div>

  <ul class="uses">
    <li>
      <svg width="52" height="30" viewBox="0 0 52 30"><path d="M4 16 H46 L40 24 H10 Z" fill="#fff"/><path d="M16 16 V8 H32 L38 16 Z" fill="#fff"/><path d="M2 28 q6 -4 12 0 t12 0 t12 0 t12 0" stroke="#fff" stroke-width="2" fill="none"/></svg>
      BOATS
    </li>
    <li>
      <svg width="52" height="52" viewBox="0 0 52 52"><circle cx="26" cy="26" r="17" fill="none" stroke="#fff" stroke-width="6" stroke-dasharray="6 4"/><circle cx="26" cy="26" r="10" fill="none" stroke="#fff" stroke-width="3"/><rect x="20" y="20" width="12" height="12" fill="#fff"/></svg>
      INDUSTRIAL STEEL<br>SURFACES
    </li>
    <li>
      <svg width="44" height="56" viewBox="0 0 44 56"><path d="M18 4 H26 V12 L38 20 H6 L18 12 Z" fill="#fff"/><rect x="10" y="26" width="24" height="28" fill="#fff"/><rect x="15" y="36" width="14" height="3" fill="var(--teal)"/></svg>
      STAINLESS STEEL<br>KITCHENS
    </li>
  </ul>

  <svg class="copy" width="869" height="1200" viewBox="0 0 869 1200">
    <text x="121" y="759" font-size="56" fill="var(--teal)" textLength="625" lengthAdjust="spacingAndGlyphs">STAINLESS STEEL</text>
    <text x="121" y="886" font-size="150" fill="var(--white)" textLength="625" lengthAdjust="spacingAndGlyphs">POLISH</text>
    <rect x="121" y="909" width="625" height="42" fill="var(--teal)"/>
    <text x="134" y="943" font-size="38" fill="var(--white)" textLength="599" lengthAdjust="spacingAndGlyphs">RESTORE STEEL SURFACES</text>
    <text x="121" y="1013" font-size="60" fill="var(--white)" textLength="625" lengthAdjust="spacingAndGlyphs">HOLOGRAM FREE</text>
    <text x="121" y="1055" font-size="24" textLength="625" lengthAdjust="spacingAndGlyphs">
      <tspan fill="var(--teal)">1. Prewash </tspan><tspan fill="var(--white)" font-size="30">2. CLEAN </tspan><tspan fill="var(--teal)">3. Protect 4. Preserve</tspan>
    </text>
    <path d="M285 1070 Q340 1062 405 1066" stroke="var(--teal)" stroke-width="3" fill="none"/>
    <text x="746" y="1139" font-size="30" fill="var(--white)" text-anchor="end" textLength="458" lengthAdjust="spacingAndGlyphs">www.kaltrochemicals.com</text>
  </svg>
</main>
</body>
</html>
```